Medspa business needs a webpage

we need a website for a new Medspa company based in Lynden, WA called Tarn Meridian Medical Aesthetics. We offer non surgical, cosmetic procedures as well as medical weight loss. We would like a sleek design, with rich colors (dark, emerald green and gold). The website should list our services, pricing and links to book appointments.

```html
<!DOCTYPE html>
<html lang="en">
<head>
<meta charset="utf-8">
<title>Tarn Meridian Medical Aesthetics</title>
<link href="https://fonts.googleapis.com/css2?family=Inter:wght@400;500;600;700&family=Playfair+Display:wght@600;700&display=swap" rel="stylesheet">
<style>
:root{
  --gold:#c4a86b;
  --gold-text:#d8b86a;
  --deep:#0f201a;
  --panel:#112620;
  --band:#132a22;
  --line:#26413a;
  --ink:#e9efe9;
  --muted:#b9c4bd;
  --dark-btn:#0b1f14;
}
*{box-sizing:border-box;margin:0;padding:0}
html,body{width:1200px;height:2529px;overflow:hidden}
body{background:var(--deep);color:var(--ink);font-family:"Inter",sans-serif;position:relative}
.serif{font-family:"Playfair Display",serif}
a{color:inherit;text-decoration:none}

.topbar{position:absolute;left:0;top:0;width:1200px;height:44px;background:var(--gold);z-index:3}
.topbar nav{position:absolute;right:48px;top:8px;display:flex;align-items:center;gap:0;font-size:12px;font-weight:600;color:#1b2118}
.topbar nav a{margin-left:46px}
.topbar .book{background:var(--dark-btn);color:var(--gold-text);padding:7px 13px;border-radius:14px;margin-left:44px}
.brand{position:absolute;left:69px;top:0;width:109px;height:92px;background:#0f2518;z-index:4;border-radius:0 0 4px 4px;display:flex;align-items:center;justify-content:center;text-align:center;color:var(--gold);font-size:10px;font-weight:500;letter-spacing:2px;line-height:1.5;padding-top:18px}

.hero{position:absolute;left:0;top:44px;width:1200px;height:543px;background:linear-gradient(90deg,#4a4424 0%,#1c2a1f 6%,var(--deep) 14%)}
.hero-photo{position:absolute;left:440px;top:0;width:760px;height:543px;background:radial-gradient(ellipse at 50% 45%,#d9b9a4 0%,#c9a58d 30%,#e8e6ec 55%,#8f95c9 70%,var(--deep) 95%)}
.hero-copy{position:absolute;left:81px;top:104px;width:380px}
.eyebrow{color:var(--gold-text);font-weight:700;font-size:19px;display:flex;align-items:center;gap:4px}
.eyebrow::after{content:"";width:34px;height:2px;background:var(--gold-text);margin-top:10px}
.hero h1{font-size:52px;line-height:58px;font-weight:700;color:#fff;margin-top:6px}
.hero p{font-size:19px;line-height:27px;margin-top:20px;color:#fff}
.hero .ctas{display:flex;gap:7px;margin-top:20px}
.btn{display:inline-block;border-radius:14px;font-size:12px;font-weight:600;padding:7px 15px}
.btn-light{background:#fff;color:#1a1a1a}
.btn-gold{background:var(--gold);color:#1b1c12}
.btn-outline{border:1px solid var(--gold);color:var(--gold-text)}

.trust{position:absolute;left:0;top:587px;width:1200px;height:54px;background:#12261f;border-bottom:1px solid var(--line);display:flex;justify-content:center;gap:6px;padding-top:11px}
.trust span{width:225px;height:32px;border:1px solid var(--line);border-radius:16px;display:flex;align-items:center;justify-content:center;font-size:10px;font-weight:700}

.section{position:absolute;left:0;width:1200px}
.wrap{position:absolute;left:256px;width:688px}
.sec-title{font-size:23px;font-weight:700;position:relative;padding-left:12px}
.sec-title::before{content:"";position:absolute;left:0;top:0;width:5px;height:5px;background:var(--gold)}
.card{border:1px solid var(--line);border-radius:8px;background:#10231d;padding:12px 11px}
.card h3{font-family:"Playfair Display",serif;font-size:13px;font-weight:700}
.card p{font-size:10px;line-height:16px;color:var(--ink);margin-top:10px}
.card ul{list-style:none;margin-top:8px}
.card li{font-size:10px;line-height:16px;margin-bottom:3px;padding-left:10px;position:relative}
.card li::before{content:"•";position:absolute;left:0}
.card .link{display:block;font-size:10px;font-weight:700;color:var(--gold-text);margin-top:6px}

.services{top:641px;height:346px}
.svc-grid{display:grid;grid-template-columns:repeat(3,1fr);gap:15px;margin-top:14px}
.svc-grid .card{height:190px}

.pricing{top:987px;height:303px;background:var(--band)}
.price-grid{display:grid;grid-template-columns:repeat(4,1fr);gap:15px;margin-top:14px}
.price-grid .card{height:171px;position:relative}
.price-grid ul{margin-top:6px}
.price-grid .btn{position:absolute;left:11px;top:134px;font-size:10px;padding:7px 14px}
.note{font-size:8px;color:var(--muted);margin-top:10px}

.providers{top:1290px;height:623px}
.prov-grid{position:absolute;left:25px;top:124px;display:flex;gap:66px}
.prov{width:286px;height:412px;border:1px solid var(--line);border-radius:8px;padding:11px}
.portrait{width:262px;height:262px;border-radius:6px;background:linear-gradient(160deg,#9a9d9e,#6e7273 60%,#2b2b2d)}
.prov h3{font-family:"Playfair Display",serif;font-size:13px;margin-top:10px}
.prov p{font-size:10px;line-height:16px;margin-top:12px}

.cta{top:1913px;height:155px;background:linear-gradient(90deg,#173027,#122a20);border-top:1px solid var(--line);border-bottom:1px solid var(--line)}
.cta h2{font-size:23px;font-weight:700}
.cta p{font-size:10px;margin-top:12px}
.cta .actions{position:absolute;right:0;top:4px;display:flex;gap:8px}
.cta .btn{font-size:10px;padding:8px 10px}

.visit{top:2068px;height:400px}
.visit .addr{font-size:10px;margin-top:30px}
.visit .dir{font-size:10px;font-weight:700;color:var(--gold-text);margin-top:14px;display:block}
.visit ul{margin-top:14px;padding-left:24px}
.visit li{font-size:10px;font-weight:700;color:var(--gold-text);line-height:16px}
.form{position:absolute;left:384px;top:40px;width:304px;height:318px;border:1px solid var(--line);border-radius:8px;padding:12px 11px}
.form label{display:block;font-size:10px;margin-bottom:6px;margin-top:0}
.field{height:26px;border:1px solid var(--line);border-radius:6px;background:#0b1a15;font-size:8px;color:#aeb8b2;padding:8px 8px;margin-bottom:12px;position:relative}
.field.sel{color:#fff}
.field.sel::after{content:"⌄";position:absolute;right:6px;top:4px;font-size:9px}
.field.area{height:55px;font-family:monospace;margin-bottom:8px}
.send{height:23px;border-radius:12px;background:var(--gold);color:#1b1c12;font-size:8px;font-weight:700;display:flex;align-items:center;justify-content:center}
.form small{display:block;font-size:8px;color:var(--muted);margin-top:12px}

.footer{top:2468px;height:61px;border-top:1px solid var(--line)}
.footer .wrap{top:31px;display:flex;justify-content:space-between;font-size:10px}
.footer nav a{margin-left:10px}
</style>
</head>
<body>

<header class="topbar">
  <nav>
    <a href="#">Home</a><a href="#">Services</a><a href="#">Team</a><a href="#">Contact</a>
    <a href="#" class="book">Book Now</a>
  </nav>
</header>
<div class="brand">TARN<br>MERIDIAN</div>

<section class="hero">
  <div class="hero-photo" role="img" aria-label="Portrait of a smiling woman with gloved provider hands framing her face"></div>
  <div class="hero-copy">
    <div class="eyebrow">ELEVATE YOUR SKIN.</div>
    <h1 class="serif">Where Natural Beauty Meets Expert Care</h1>
    <p>Non-surgical aesthetic treatments and medical weight loss in Lynden, WA.</p>
    <div class="ctas"><a class="btn btn-light" href="#">Book an Appointment</a><a class="btn btn-gold" href="#">Explore Services</a></div>
  </div>
</section>

<div class="trust"><span>Board-Certified Providers</span><span>Medical-Grade Treatments</span><span>Personalized Care Plans</span></div>

<section class="section services">
  <div class="wrap" style="top:47px">
    <h2 class="sec-title serif">Our Services</h2>
    <div class="svc-grid">
      <div class="card"><h3>Injectables</h3><p>Neuromodulators and dermal fillers to smooth lines, restore volume, and refine contours.</p><ul><li>Neurotoxin A / Neurotoxin B</li><li>Lip &amp; Cheek Filler</li><li>Jawline &amp; Chin Contour</li></ul><a class="link" href="#">Book injectables →</a></div>
      <div class="card"><h3>Skin Rejuvenation</h3><p>Treat texture, tone, and radiance with non-invasive solutions and minimal downtime.</p><ul><li>Microneedling</li><li>Medical-grade Peels</li><li>LED &amp; Collagen Therapy</li></ul><a class="link" href="#">Book skin rejuvenation →</a></div>
      <div class="card"><h3>Medical Weight Loss</h3><p>Clinically guided programs tailored to your goals with ongoing provider support.</p><ul><li>Consultation &amp; Labs</li><li>GLP-1 Assisted Plans</li><li>Nutrition &amp; Coaching</li></ul><a class="link" href="#">Book weight loss consult →</a></div>
    </div>
  </div>
</section>

<section class="section pricing">
  <div class="wrap" style="top:48px">
    <h2 class="sec-title serif">Transparent Pricing</h2>
    <div class="price-grid">
      <div class="card"><h3>Neuromodulators</h3><ul><li>Forehead, Glabella, Crow's Feet</li><li>Treatment plan review</li><li>Follow-up tweak within 2 weeks</li></ul><a class="btn btn-gold" href="#">Start Now</a></div>
      <div class="card"><h3>Dermal Fillers</h3><ul><li>Lips, Cheeks, Jawline, Chin</li><li>Includes numbing &amp; aftercare</li><li>1:1 aesthetic mapping</li></ul><a class="btn btn-gold" href="#">Start Now</a></div>
      <div class="card"><h3>Microneedling</h3><ul><li>Face &amp; Neck</li><li>Medical-grade serums</li><li>Series packages available</li></ul><a class="btn btn-gold" href="#">Start Now</a></div>
      <div class="card"><h3>Weight Loss Program</h3><ul><li>Provider consult &amp; labs</li><li>Medication when appropriate</li><li>Coaching &amp; check-ins</li></ul><a class="btn btn-gold" href="#">Start Now</a></div>
    </div>
    <p class="note">* Pricing shown for contest demo. Final quotes provided after consultation.</p>
  </div>
</section>

<section class="section providers">
  <div class="wrap" style="top:74px">
    <h2 class="sec-title serif">Meet Your Providers</h2>
    <div class="prov-grid" style="top:50px">
      <div class="prov"><div class="portrait" role="img" aria-label="Headshot of provider Lena Varrow"></div><h3>Lena Varrow, DNP</h3><p>Lena combines her doctoral training and medical background to deliver precision-driven aesthetic and wellness services. With a focus on patient education and natural results, she ensures every client feels confident in their journey.</p></div>
      <div class="prov"><div class="portrait" role="img" aria-label="Headshot of provider Maren Quill"></div><h3>Maren Quill, ARNP</h3><p>Maren brings years of experience as a family nurse practitioner, blending advanced clinical expertise with a warm, personalized approach to patient care. She is dedicated to helping clients look and feel their best through safe, evidence based treatments.</p></div>
    </div>
  </div>
</section>

<section class="section cta">
  <div class="wrap" style="top:47px">
    <h2 class="serif">Ready to glow?</h2>
    <p>Reserve your appointment in minutes. New patients welcome.</p>
    <div class="actions"><a class="btn btn-gold" href="#">Book Online</a><a class="btn btn-outline" href="#">Call (360) 555-0187</a></div>
  </div>
</section>

<section class="section visit">
  <div class="wrap" style="top:52px">
    <h2 class="sec-title serif">Visit Us</h2>
    <p class="addr">4120 Alder Crest Way Suite 8, Lynden, WA 98264</p>
    <a class="dir" href="#">Get directions →</a>
    <ul><li>Call: (360) 555-0187</li><li>Email: hello@tarnmeridian.com</li><li>Book online</li></ul>
    <div class="form" style="top:-12px">
      <label>Name</label><div class="field">Your full name</div>
      <label>Email</label><div class="field">you@example.com</div>
      <label>Service</label><div class="field sel">Injectables</div>
      <label>Message</label><div class="field area">Tell us your goals</div>
      <div class="send">Send Message</div>
      <small>Demo form for contest—replace with platform form or CRM embed.</small>
    </div>
  </div>
</section>

<footer class="section footer">
  <div class="wrap"><span>© 2025 Tarn Meridian Medical Aesthetics • Lynden, WA</span><nav><a href="#">Services</a><a href="#">Book</a><a href="#">Privacy</a></nav></div>
</footer>

</body>
</html>
```